MEDIA KIT RE-DESIGN

TAKE A CURRENT POWER POINT FILE AND GIVE IT A FRESH LOOK/REBRAND USING CONTENT AND PHOTOS ETC IN THE PROVIDED FILE WITH THE EXCEPTION OF THE TITLE PAGE WHICH CAN BE BRAND NEW.

```html
<!DOCTYPE html>
<html lang="en">
<head>
<meta charset="utf-8">
<title>Lumen Media Network — Media Kit</title>
<link href="https://fonts.googleapis.com/css2?family=Montserrat:wght@400;700&family=Roboto:wght@400;700&display=swap" rel="stylesheet">
<style>
:root{
  --red:#c00000;
  --dark:#1d1d1d;
  --ink:#222;
  --grey:#777;
  --light:#e9e8ea;
  --white:#fff;
}
*{box-sizing:border-box;margin:0;padding:0}
html,body{width:713px;height:1200px;overflow:hidden;background:var(--light);font-family:Roboto,sans-serif;color:var(--ink)}
.sheet{position:relative;width:713px;height:1200px}
.slide{position:absolute;width:321px;height:180px;background:var(--white);overflow:hidden}
.abs{position:absolute}
.photo-dark{background:linear-gradient(180deg,#2b2b2b,#161616 70%,#262626)}
.h-title{position:absolute;left:0;right:0;top:12px;text-align:center;font-family:Montserrat,sans-serif;font-size:11px;color:var(--ink)}
.h-title b{color:var(--red)}
.h-title.light{color:var(--white)}
.brand{font-family:Montserrat,sans-serif;font-weight:700;color:#555;letter-spacing:.2px}
.brand small{display:block;font-weight:400;font-size:.45em;letter-spacing:1.5px;text-align:right}
.footer .brand{position:absolute;left:7px;top:166px;font-size:7px;color:#555}
.footer .bar{position:absolute;left:60px;top:167px;width:253px;height:7px;background:var(--red);border-radius:4px;color:var(--white);font-size:3.3px;line-height:7px;text-align:right;padding-right:8px}
.ico{position:absolute;width:21px;height:21px;border-radius:50%;background:var(--red);border:2px solid var(--white);box-shadow:0 0 0 .5px #ccc;display:flex;align-items:center;justify-content:center}
.ico svg{width:10px;height:10px}
.lbl{position:absolute;width:46px;text-align:center;font-size:5.4px;line-height:6.4px}
.lbl b{color:var(--red)}
.divider{position:absolute;top:116px;width:.5px;height:30px;background:#ddd}
.cap{position:absolute;left:0;right:0;bottom:4px;text-align:center;font-size:3.6px;color:#888;letter-spacing:.3px}
.kiosk{position:absolute;background:linear-gradient(180deg,#5a3a1c 0%,#2c241d 45%,#e7e7e7 70%,#f4f4f4);border-radius:3px}
.hero-title{position:absolute;left:29px;top:78px;font-family:Montserrat,sans-serif;font-weight:700;font-size:16px;color:var(--white)}
.hero-sub{position:absolute;left:29px;top:97px;font-family:Montserrat,sans-serif;font-size:10px;color:var(--white)}
.hero-btn{position:absolute;left:29px;top:128px;width:73px;height:10px;background:var(--red);color:var(--white);font-size:3.8px;line-height:10px;text-align:center;font-weight:700;letter-spacing:.3px}
.list-row{position:absolute;left:165px;display:flex;align-items:center;gap:5px;font-size:5.4px}
.list-row .ico{position:static;width:17px;height:17px}
.list-row .ico svg{width:8px;height:8px}
.tgt{position:absolute;left:36px;width:130px;display:flex;gap:6px}
.tgt .ico{position:static;flex:none;width:17px;height:17px}
.tgt .ico svg{width:8px;height:8px}
.tgt h4{font-family:Montserrat,sans-serif;font-size:5.2px;color:var(--red)}
.tgt p{font-size:3.5px;line-height:4.2px}
.net-card{position:absolute;top:42px;width:86px;height:100px;background:var(--red);border-radius:4px;overflow:hidden;color:var(--white)}
.net-card .pic{height:42px}
.net-card .ico{left:32px;top:32px;background:#777}
.net-card h5{margin-top:14px;text-align:center;font-family:Montserrat,sans-serif;font-size:6px}
.net-card .sub{text-align:center;font-size:3.5px}
.net-card ul{margin:5px 0 0 12px;font-size:3.5px;line-height:5.6px}
.venue{position:absolute;top:37px;width:87px;text-align:center}
.venue .pic{height:42px;border:1.5px solid var(--white)}
.venue h5{margin-top:5px;font-family:Montserrat,sans-serif;font-size:5.2px;color:var(--red)}
.venue ul{text-align:left;margin:4px 0 0 10px;font-size:3.2px;line-height:4.6px;color:#666}
.venue .mark{width:42px;height:18px;margin:5px auto 0;border:.5px solid #ddd;border-radius:3px;display:flex;align-items:center;justify-content:center}
.venue .mark i{display:block;width:8px;height:8px;background:#aaa;border-radius:50%}
.venue .url{margin-top:5px;font-size:3.5px;color:var(--red)}
.thumb{position:absolute;width:43px;height:60px}
.stat{position:absolute;width:60px;text-align:center;font-size:5.4px}
.stat .ico{position:relative;left:auto;top:auto;margin:0 auto 3px;width:20px;height:20px}
.stat .num{font-family:Montserrat,sans-serif;font-weight:700;font-size:16px;line-height:18px}
.stat .num span{font-weight:400;font-size:10px}
.contact{position:absolute;left:29px;top:98px;color:var(--white)}
.contact h3{font-family:Montserrat,sans-serif;font-size:8px;margin-bottom:8px}
.contact p{font-size:4.5px;line-height:9px;display:flex;align-items:center;gap:5px}
.contact svg{width:5px;height:5px}
</style>
</head>
<body>
<svg width="0" height="0" style="position:absolute">
  <defs>
    <g id="i-screen"><rect x="3" y="1" width="6" height="8" rx="1" fill="none" stroke="#fff" stroke-width="1.2"/><rect x="5.5" y="9" width="1" height="2" fill="#fff"/></g>
    <g id="i-pin"><path d="M6 11 C2 6 2 4 2 4 A4 4 0 0 1 10 4 C10 6 6 11 6 11Z" fill="none" stroke="#fff" stroke-width="1.2"/><circle cx="6" cy="4.2" r="1.3" fill="#fff"/></g>
    <g id="i-bag"><rect x="1.5" y="3.5" width="9" height="7" rx="1" fill="#fff"/><rect x="4" y="1.5" width="4" height="2.5" fill="none" stroke="#fff"/></g>
    <g id="i-globe"><circle cx="6" cy="6" r="4.5" fill="none" stroke="#fff" stroke-width="1.1"/><ellipse cx="6" cy="6" rx="2" ry="4.5" fill="none" stroke="#fff" stroke-width=".8"/><line x1="1.5" y1="6" x2="10.5" y2="6" stroke="#fff" stroke-width=".8"/></g>
    <g id="i-dollar"><text x="6" y="9.5" text-anchor="middle" font-size="10" font-weight="700" fill="#fff" font-family="Roboto,sans-serif">$</text></g>
    <g id="i-bars"><rect x="2" y="7" width="2" height="3" fill="#fff"/><rect x="5" y="5" width="2" height="5" fill="#fff"/><rect x="8" y="2" width="2" height="8" fill="#fff"/></g>
    <g id="i-x"><path d="M3 3 L9 9 M9 3 L3 9" stroke="#fff" stroke-width="1.8"/></g>
    <g id="i-person"><circle cx="6" cy="4" r="2.2" fill="#fff"/><path d="M2 11 C2 7 10 7 10 11Z" fill="#fff"/></g>
    <g id="i-gear"><circle cx="6" cy="6" r="4" fill="none" stroke="#fff" stroke-width="1.8" stroke-dasharray="1.5 1"/><circle cx="6" cy="6" r="1.6" fill="#fff"/></g>
    <g id="i-star"><circle cx="6" cy="5" r="3.5" fill="#fff"/><path d="M4 8 L3 11 L6 9.5 L9 11 L8 8Z" fill="#fff"/></g>
    <g id="i-people"><circle cx="4" cy="4.5" r="1.6" fill="#fff"/><circle cx="8" cy="4.5" r="1.6" fill="#fff"/><path d="M1 10 C1 7 7 7 7 10Z M5 10 C5 7 11 7 11 10Z" fill="#fff"/></g>
    <g id="i-image"><rect x="2" y="2.5" width="8" height="7" fill="none" stroke="#fff" stroke-width="1.1"/><path d="M3 9 L5.5 6 L7 7.5 L8 6.5 L9.5 9Z" fill="#fff"/></g>
    <g id="i-tag"><path d="M2 6 L6 2 L10 2 L10 6 L6 10Z" fill="#fff"/><circle cx="8.3" cy="3.7" r=".8" fill="var(--red)"/></g>
    <g id="i-cap"><path d="M1 5 L6 2.5 L11 5 L6 7.5Z" fill="#fff"/><path d="M3.5 6.5 V9 C5 10.3 7 10.3 8.5 9 V6.5" fill="#fff"/></g>
    <g id="i-run"><circle cx="7.5" cy="2.3" r="1.4" fill="#fff"/><path d="M3 6 L6 4 L8 5.5 L7 8 L9 11 M6 6.5 L4 10.5" stroke="#fff" stroke-width="1.2" fill="none"/></g>
    <g id="i-table"><rect x="2" y="4" width="8" height="1.5" fill="#fff"/><path d="M3 5.5 V10 M9 5.5 V10" stroke="#fff" stroke-width="1.1"/></g>
    <g id="i-news"><rect x="2" y="2" width="8" height="8" fill="none" stroke="#fff" stroke-width="1.1"/><path d="M3.5 4.5 H8.5 M3.5 6.2 H8.5 M3.5 7.9 H7" stroke="#fff" stroke-width=".8"/></g>
    <g id="i-radio"><rect x="1.5" y="4" width="9" height="6" rx="1" fill="none" stroke="#fff" stroke-width="1.1"/><circle cx="4.5" cy="7" r="1.3" fill="#fff"/><path d="M3 4 L9 1.5" stroke="#fff"/></g>
    <g id="i-tv"><rect x="1.5" y="3.5" width="9" height="6.5" rx="1" fill="none" stroke="#fff" stroke-width="1.1"/><path d="M4 1.5 L6 3.5 L8 1.5" stroke="#fff" fill="none"/></g>
  </defs>
</svg>

<main class="sheet">

  <!-- 1 Title with kiosk -->
  <section class="slide" style="left:30px;top:31px">
    <div class="brand abs" style="left:17px;top:14px;font-size:15px">LumenMedia<small>NETWORK</small></div>
    <svg class="abs" style="left:0;top:0" width="321" height="180"><polygon points="0,52 162,52 177,28 321,28 321,168 0,168" fill="#1f1f1f"/></svg>
    <div class="abs photo-dark" role="img" aria-label="Dim corridor with a wall billboard and stairs" style="left:0;top:52px;width:321px;height:116px;opacity:.55"></div>
    <div class="hero-title">Indoor Advertising</div>
    <div class="hero-sub">That Engages Audiences</div>
    <div class="hero-btn">WWW.LUMENMEDIA.CA</div>
    <div class="kiosk" role="img" aria-label="Freestanding digital kiosk showing a food advertisement" style="left:219px;top:8px;width:60px;height:164px"></div>
    <div class="cap">© 2017 Lumen Media Network. All Rights Reserved.</div>
  </section>

  <!-- 2 Title -->
  <section class="slide" style="left:362px;top:31px">
    <div class="brand abs" style="left:17px;top:14px;font-size:15px">LumenMedia<small>NETWORK</small></div>
    <svg class="abs" style="left:0;top:0" width="321" height="180"><polygon points="0,52 162,52 177,28 321,28 321,168 0,168" fill="#1f1f1f"/></svg>
    <div class="abs" role="img" aria-label="Dim corridor with a lit food billboard on the wall" style="left:120px;top:60px;width:201px;height:100px;background:radial-gradient(ellipse at 60% 50%,#5a4020,#222 70%);opacity:.8"></div>
    <div class="hero-title">Indoor Advertising</div>
    <div class="hero-sub">That Engages Audiences</div>
    <div class="hero-btn">WWW.LUMENMEDIA.CA</div>
    <div class="cap">© 2017 Lumen Media Network. All Rights Reserved.</div>
  </section>

  <!-- 3 About -->
  <section class="slide" style="left:30px;top:222px">
    <div class="h-title"><b>About</b> Us</div>
    <div class="abs photo-dark" role="img" aria-label="Corridor with a wall billboard" style="left:0;top:36px;width:321px;height:64px"></div>
    <div class="ico" style="left:23px;top:89px"><svg viewBox="0 0 12 12"><use href="#i-bag"/></svg></div>
    <div class="ico" style="left:74px;top:89px"><svg viewBox="0 0 12 12"><use href="#i-screen"/></svg></div>
    <div class="ico" style="left:125px;top:89px"><svg viewBox="0 0 12 12"><use href="#i-pin"/></svg></div>
    <div class="ico" style="left:176px;top:89px"><svg viewBox="0 0 12 12"><use href="#i-screen"/></svg></div>
    <div class="ico" style="left:227px;top:89px"><svg viewBox="0 0 12 12"><use href="#i-globe"/></svg></div>
    <div class="ico" style="left:278px;top:89px"><svg viewBox="0 0 12 12"><use href="#i-dollar"/></svg></div>
    <div class="divider" style="left:59px"></div>
    <div class="divider" style="left:110px"></div>
    <div class="divider" style="left:161px"></div>
    <div class="divider" style="left:212px"></div>
    <div class="divider" style="left:263px"></div>
    <div class="lbl" style="left:10.5px;top:118px">Established in<br><b>1996.</b></div>
    <div class="lbl" style="left:61.5px;top:118px">Offer Effective<br><b>Indoor Media.</b></div>
    <div class="lbl" style="left:112.5px;top:118px">Offer <b>High-<br>traffic</b><br>Locations.</div>
    <div class="lbl" style="left:163.5px;top:118px">Offer<br><b>Strategically</b><br>Placed<br>Billboards.</div>
    <div class="lbl" style="left:214.5px;top:118px">Offer Three<br>Distinct<br><b>Networks.</b></div>
    <div class="lbl" style="left:265.5px;top:118px">Offer<br>Experience In<br>Selling<br><b>Sponsorship.</b></div>
    <div class="footer"><div class="brand">LumenMedia</div><div class="bar">© 2017 Lumen Media Network. All Rights Reserved. &nbsp;|&nbsp; 3</div></div>
  </section>

  <!-- 4 Why Billboards -->
  <section class="slide photo-dark" style="left:362px;top:222px" role="img" aria-label="Corridor with wall billboard and stairs">
    <div class="abs" style="left:160px;top:0;width:161px;height:165px;background:var(--white)"></div>
    <div class="abs" style="left:40px;top:66px;width:80px;text-align:center;font-family:Montserrat,sans-serif;font-size:10px;color:#fff;line-height:12px">Why<br><b>Billboards?</b></div>
    <div class="list-row" style="top:24px"><span class="ico"><svg viewBox="0 0 12 12"><use href="#i-star"/></svg></span>Guaranteed Readership</div>
    <div class="list-row" style="top:49px"><span class="ico"><svg viewBox="0 0 12 12"><use href="#i-person"/></svg></span>100% Gender Specific</div>
    <div class="list-row" style="top:74px"><span class="ico"><svg viewBox="0 0 12 12"><use href="#i-gear"/></svg></span>Captive Environment</div>
    <div class="list-row" style="top:99px"><span class="ico"><svg viewBox="0 0 12 12"><use href="#i-x"/></svg></span>No Clutter</div>
    <div class="list-row" style="top:124px"><span class="ico"><svg viewBox="0 0 12 12"><use href="#i-bars"/></svg></span>High Frequency</div>
    <div class="kiosk" role="img" aria-label="Freestanding digital kiosk" style="left:250px;top:13px;width:52px;height:142px"></div>
    <div class="footer"><div class="brand" style="color:#fff">LumenMedia</div><div class="bar">© 2017 Lumen Media Network. All Rights Reserved. &nbsp;|&nbsp; 4</div></div>
  </section>

  <!-- 5 Why Wallboards -->
  <section class="slide" style="left:30px;top:413px">
    <div class="h-title">Why <b>Wallboards?</b></div>
    <div class="abs photo-dark" style="left:0;top:36px;width:321px;height:82px"></div>
    <div class="abs" role="img" aria-label="Arena wallboard advertisement under spotlights" style="left:77px;top:53px;width:59px;height:44px;background:linear-gradient(135deg,#cfc9b4,#8f8a78)"></div>
    <div class="abs" role="img" aria-label="Rink-side wallboard advertisement" style="left:188px;top:53px;width:56px;height:44px;background:linear-gradient(135deg,#f2f2f2,#bcc3d6)"></div>
    <div class="ico" style="left:47px;top:107px"><svg viewBox="0 0 12 12"><use href="#i-screen"/></svg></div>
    <div class="ico" style="left:116px;top:107px"><svg viewBox="0 0 12 12"><use href="#i-image"/></svg></div>
    <div class="ico" style="left:185px;top:107px"><svg viewBox="0 0 12 12"><use href="#i-bars"/></svg></div>
    <div class="ico" style="left:254px;top:107px"><svg viewBox="0 0 12 12"><use href="#i-tag"/></svg></div>
    <div class="lbl" style="left:34.5px;top:135px"><b>48" X 96"</b><br>Billboard</div>
    <div class="lbl" style="left:103.5px;top:135px">Full <b>Colour</b></div>
    <div class="lbl" style="left:172.5px;top:135px">High <b>Impact</b></div>
    <div class="lbl" style="left:241.5px;top:135px">Brand<br><b>Awareness</b></div>
    <div class="abs" style="left:0;right:0;top:154px;text-align:center;font-size:3.6px">* Available at Riverton Arenas.</div>
    <div class="footer"><div class="brand">LumenMedia</div><div class="bar">© 2017 Lumen Media Network. All Rights Reserved. &nbsp;|&nbsp; 5</div></div>
  </section>

  <!-- 6 Targeting -->
  <section class="slide" style="left:362px;top:413px">
    <div class="h-title"><b>Targeting</b> Abilities</div>
    <div class="tgt" style="top:46px"><span class="ico"><svg viewBox="0 0 12 12"><use href="#i-people"/></svg></span><div><h4>Captive Audience</h4><p>There are few, if any, other places that allow you to deliver your message with so little distraction.</p></div></div>
    <div class="tgt" style="top:72px"><span class="ico"><svg viewBox="0 0 12 12"><use href="#i-screen"/></svg></span><div><h4>100% Gender Specific</h4><p>Compared to all other traditional media, classic billboards are the only media that can offer this.</p></div></div>
    <div class="tgt" style="top:98px"><span class="ico"><svg viewBox="0 0 12 12"><use href="#i-bars"/></svg></span><div><h4>Better Recall</h4><p>They are able to recall your message for 60% to 80% longer than other types of advertising.</p></div></div>
    <div class="tgt" style="top:124px"><span class="ico"><svg viewBox="0 0 12 12"><use href="#i-bars"/></svg></span><div><h4>Affordable</h4><p>Less expensive than many traditional forms of marketing which delivers you a better return on your investment.</p></div></div>
    <div class="abs" role="img" aria-label="Illustration of a red and white target hit by an arrow" style="left:172px;top:50px;width:118px;height:82px;background:linear-gradient(135deg,#f6e3e3,#d42a2a)"></div>
    <div class="footer"><div class="brand">LumenMedia</div><div class="bar">© 2017 Lumen Media Network. All Rights Reserved. &nbsp;|&nbsp; 6</div></div>
  </section>

  <!-- 7 Networks -->
  <section class="slide" style="left:30px;top:604px">
    <div class="h-title" style="font-weight:700">Networks</div>
    <div class="net-card" style="left:21px"><div class="pic" role="img" aria-label="Restaurant and sports bar exterior" style="background:linear-gradient(135deg,#8a2a24,#4b3a33)"></div><div class="ico"><svg viewBox="0 0 12 12"><use href="#i-table"/></svg></div><h5>RESTOBAR</h5><div class="sub">40 + LOCATIONS</div><ul><li>Riverton</li><li>Vernon</li><li>Kelowna</li><li>Penticton</li></ul></div>
    <div class="net-card" style="left:117px"><div class="pic" role="img" aria-label="Busy university campus hall" style="background:linear-gradient(135deg,#6f7a80,#3b3f44)"></div><div class="ico"><svg viewBox="0 0 12 12"><use href="#i-cap"/></svg></div><h5>CAMPUS</h5><div class="sub">9 BUILDINGS</div><ul><li>Northbridge University Riverton, BC</li><li>Lakeview University Kelowna, BC</li></ul></div>
    <div class="net-card" style="left:213px"><div class="pic" role="img" aria-label="Basketball game in a gymnasium" style="background:linear-gradient(135deg,#5a4c48,#2e3140)"></div><div class="ico"><svg viewBox="0 0 12 12"><use href="#i-run"/></svg></div><h5>SPORTS</h5><div class="sub">3 VENUES</div><ul><li>Summit Arena</li><li>Riverton, BC</li></ul></div>
    <div class="footer"><div class="brand">LumenMedia</div><div class="bar">© 2017 Lumen Media Network. All Rights Reserved. &nbsp;|&nbsp; 7</div></div>
  </section>

  <!-- 8 Sport & Arena -->
  <section class="slide" style="left:362px;top:604px">
    <div class="abs photo-dark" style="left:0;top:0;width:321px;height:57px"></div>
    <div class="h-title light"><b style="color:#fff">Sport</b> &amp; <b style="color:#fff">Arena</b></div>
    <div class="venue" style="left:16px"><div class="pic" role="img" aria-label="Aerial view of a sports centre with running track" style="background:linear-gradient(135deg,#7d8a74,#a33b33)"></div><h5>Riverside Sports Centre</h5><ul><li>NBU Varsity Men &amp; Women Soccer</li><li>NBU Varsity Men &amp; Women Basketball</li><li>NBU Varsity Men &amp; Volleyball</li><li>Aquatic, Track &amp; Gymnastics Centre</li><li>1,000,000 visitors per year</li></ul><div class="mark"><i></i></div><div class="url">www.riversidesports.ca</div></div>
    <div class="venue" style="left:117px"><div class="pic" role="img" aria-label="Arena entrance under blue sky" style="background:linear-gradient(180deg,#3e6fb3,#8d9aa8)"></div><h5>Summit Arena</h5><ul><li>River City Blazers Hockey</li><li>Riverton Minor Hockey</li><li>Concerts &amp; Trade Shows</li><li>85 Event Days</li><li>450,000 visitors per year</li></ul><div class="mark"><i></i></div><div class="url">www.summitarena.ca</div></div>
    <div class="venue" style="left:219px"><div class="pic" role="img" aria-label="Glass-fronted recreation centre" style="background:linear-gradient(180deg,#9fb2c4,#5c7a5e)"></div><h5>Island Park Centre</h5><ul><li>Riverton Minor Hockey</li><li>Riverton Bantam Tourney</li><li>Riverton Recreational Hockey</li><li>Curling Club &amp; Trade Shows</li><li>200,000 visitors per year</li></ul><div class="mark"><i></i></div><div class="url">www.riversidesports.ca</div></div>
    <div class="footer"><div class="brand">LumenMedia</div><div class="bar">© 2017 Lumen Media Network. All Rights Reserved. &nbsp;|&nbsp; 8</div></div>
  </section>

  <!-- 9 Campus -->
  <section class="slide" style="left:30px;top:795px">
    <div class="abs photo-dark" style="left:0;top:0;width:321px;height:57px"></div>
    <div class="h-title light" style="font-weight:700">Campus</div>
    <div class="venue" style="left:66px"><div class="pic" role="img" aria-label="University building with students on the lawn" style="background:linear-gradient(180deg,#a9c0d6,#5b7a4b)"></div><h5>Northbridge University</h5><ul><li>On campus students: 14,099</li><li>Male: 43% | Female: 57%</li><li>International Students: 3,635</li><li>On campus housing for 1,000</li><li>(8) Varsity Athletic teams</li></ul><div class="mark"><i></i></div><div class="url">www.northbridge.ca/venues</div></div>
    <div class="venue" style="left:167px"><div class="pic" role="img" aria-label="Varsity team huddle in a gym" style="background:linear-gradient(135deg,#3a3f57,#8b8b8b)"></div><h5>Lakeview University</h5><ul><li>On campus students: 8,218</li><li>Male: 40% | Female: 60%</li><li>On campus housing for 1,600</li><li>(8) Varsity Athletic teams</li></ul><div class="mark" style="margin-top:9px"><i></i></div><div class="url">rec.lakeview.ca/gymnasium</div></div>
    <div class="footer"><div class="brand">LumenMedia</div><div class="bar">© 2017 Lumen Media Network. All Rights Reserved. &nbsp;|&nbsp; 9</div></div>
  </section>

  <!-- 10 Past Campaigns -->
  <section class="slide" style="left:362px;top:795px">
    <div class="abs" style="left:14px;top:70px;width:90px;text-align:center;font-family:Montserrat,sans-serif;font-size:10px;line-height:12px"><b style="color:var(--red)">Past</b><br>Campaigns</div>
    <div class="thumb" role="img" aria-label="Poster campaign with a man in a jacket" style="left:111px;top:19px;background:linear-gradient(180deg,#556,#223)"></div>
    <div class="thumb" role="img" aria-label="Yellow fees poster campaign" style="left:160px;top:19px;background:linear-gradient(180deg,#f5e21a,#e9c812)"></div>
    <div class="thumb" role="img" aria-label="Student adventure poster campaign" style="left:209px;top:19px;background:linear-gradient(180deg,#9bb3c9,#7a4a7a)"></div>
    <div class="thumb" role="img" aria-label="Spa treatment poster campaign" style="left:258px;top:19px;background:linear-gradient(180deg,#e6e3e4,#a9b0b8)"></div>
    <div class="thumb" role="img" aria-label="Green volunteer poster campaign" style="left:111px;top:85px;background:linear-gradient(180deg,#2f6e4a,#1c3d2c)"></div>
    <div class="thumb" role="img" aria-label="Orange accounting poster campaign" style="left:160px;top:85px;background:linear-gradient(180deg,#ef8a3c,#d8672a)"></div>
    <div class="thumb" role="img" aria-label="Rafting trip poster campaign" style="left:209px;top:85px;background:linear-gradient(180deg,#6d8fb8,#f1f1f1)"></div>
    <div class="thumb" role="img" aria-label="Outdoor club schedule poster" style="left:258px;top:85px;background:linear-gradient(180deg,#f2f2f2,#1f3b66)"></div>
    <div class="footer"><div class="brand">LumenMedia</div><div class="bar">© 2017 Lumen Media Network. All Rights Reserved. &nbsp;|&nbsp; 10</div></div>
  </section>

  <!-- 11 Popular Media -->
  <section class="slide" style="left:30px;top:986px">
    <div class="stat" style="left:21px;top:22px"><div class="ico" style="background:#222"><svg viewBox="0 0 12 12"><use href="#i-news"/></svg></div>Newspapers<div class="num">21<span>%</span></div></div>
    <div class="stat" style="left:21px;top:97px"><div class="ico" style="background:#555"><svg viewBox="0 0 12 12"><use href="#i-radio"/></svg></div>Radio<div class="num" style="color:#444">24<span>%</span></div></div>
    <div class="stat" style="left:240px;top:22px;color:var(--red)"><div class="ico"><svg viewBox="0 0 12 12"><use href="#i-screen"/></svg></div>Indoor Billboards<div class="num">79<span>%</span></div></div>
    <div class="stat" style="left:240px;top:97px;color:#888"><div class="ico" style="background:#999"><svg viewBox="0 0 12 12"><use href="#i-tv"/></svg></div>TV<div class="num">46<span>%</span></div></div>
    <svg class="abs" style="left:110px;top:37px" width="100" height="104" viewBox="0 0 100 104">
      <g transform="rotate(-90 50 52)" fill="none" stroke-width="12">
        <circle cx="50" cy="52" r="44" stroke="#c00000" stroke-dasharray="128.7 147.8"/>
        <circle cx="50" cy="52" r="44" stroke="#9a9a9a" stroke-dasharray="75 201.5" stroke-dashoffset="-129.7"/>
        <circle cx="50" cy="52" r="44" stroke="#555" stroke-dasharray="38 238.5" stroke-dashoffset="-205.7"/>
        <circle cx="50" cy="52" r="44" stroke="#111" stroke-dasharray="31.8 244.7" stroke-dashoffset="-244.7"/>
      </g>
      <text x="50" y="49" text-anchor="middle" font-family="Montserrat,sans-serif" font-size="11" fill="#222">Popular</text>
      <text x="50" y="61" text-anchor="middle" font-family="Montserrat,sans-serif" font-weight="700" font-size="11" fill="#c00000">Media</text>
      <text x="83" y="46" font-size="3.5" fill="#fff" font-family="Roboto,sans-serif">79%</text>
      <text x="26" y="90" font-size="3.5" fill="#fff" font-family="Roboto,sans-serif">46%</text>
      <text x="7" y="40" font-size="3.5" fill="#fff" font-family="Roboto,sans-serif">24%</text>
      <text x="31" y="13" font-size="3.5" fill="#fff" font-family="Roboto,sans-serif">21%</text>
    </svg>
    <div class="footer"><div class="brand">LumenMedia</div><div class="bar">© 2017 Lumen Media Network. All Rights Reserved. &nbsp;|&nbsp; 11</div></div>
  </section>

  <!-- 12 Contact -->
  <section class="slide" style="left:362px;top:986px">
    <div class="brand abs" style="right:17px;top:14px;font-size:15px">LumenMedia<small>NETWORK</small></div>
    <svg class="abs" style="left:0;top:0" width="321" height="180"><polygon points="0,28 159,28 174,52 321,52 321,168 0,168" fill="#1f1f1f"/></svg>
    <div class="abs" role="img" aria-label="Dim corridor with a wall billboard" style="left:120px;top:60px;width:201px;height:100px;background:radial-gradient(ellipse at 55% 55%,#4a3820,#1f1f1f 70%)"></div>
    <div class="contact">
      <h3>Contact Us</h3>
      <p><svg viewBox="0 0 12 12"><path d="M3 1 L5 4 L4 5.5 C5 7.5 6 8.5 7 9 L8.5 8 L11 10 L9.5 11.5 C5 11 1 7 1 2.5Z" fill="#fff"/></svg>250-555-0148</p>
      <p><svg viewBox="0 0 12 12"><circle cx="6" cy="6" r="4.5" fill="none" stroke="#fff" stroke-width="1.3"/><circle cx="6" cy="6" r="1.8" fill="#fff"/></svg>sam@lumenmedia.ca</p>
      <p><svg viewBox="0 0 12 12"><use href="#i-globe"/></svg>www.lumenmedia.ca</p>
    </div>
    <div class="cap">© 2017 Lumen Media Network. All Rights Reserved.</div>
  </section>

</main>
</body>
</html>
```